3 images for 3 products

Hopefully, nice and easy project.

New website under construction - www.deskvigor.co.uk selling a new type of office chair

The home page has a space for a large (674*327) gallery slider containing 3 images which will rotate in a loop. In that space I would like to put something relevant to the products (the 3 products are shown in the 3 boxes just below the large white space). At the moment, as you can see there is a large void which needs to be filled and all attempts that I have tried so far have been very amateurish

***Update***
Nice entry. Its not-animated banner and banner is probably the wrong word for this although is is the category that seemed to best fit.
I updated the site last night and if you have a look at the site at the moment its the main image(s) that needs to be replaced. Currently the slider is showing 2 images ("Modrun Pottery" and "Elegent Tapestry") These are the ones that need replacing with the 3 images
***********

The product then, is a type of seating that promotes good posture and activity as you are sitting on a ball on wheels that requires core stability muscles to be engaged

Here's how similar sites sell these chairs:-
http://www.pivotrumseat.com
http://www.torvexa.com/product/exercise-ball-wobblorb-chair.do
http://www.spineward.co.uk/perchly?gclid=CNrtlMbWzKkCFYpA4QodizANMg
spineward.com

If you need to understand a bit more about the chairs it's here as I have them for sale on Marketnook:-
http://www.marketnook.co.uk/Desk-Vigor-Exercise-Chair-Black/dp/X7731KQ2ZP/ref=sr_1_1?ie=UTF8&qid=1308854474&sr=8-1

The things that are fixed which I guess you will need to work with are:-
* the colours of the deskvigor logo
* the size of the space (674*327)
* possibly the colours that you already see on the site

Things which I guess I need to see although keeping an open mind are:-
* the 3 products in rotation

Other than that it's fairly free for you to work your magic

Thanks
Derek
Updates

A good example of how the 3 image slider works is here:-

http://www.thornwickstudio.com/

A further point I should have mentioned is that although the contest is due to run until July 3, I will probably be ending it before that date as I need to fill the blank space as the products are now live on Marketnook

Not sure if this helps but keywords that describe the product are:-
stability ball chair
posture ball chair
office fitness
active seating

Target Market(s)

Adults 20-60, typically office workers

Industry/Entity Type

Construction

Requirements
Must have
• Images of balls

```html
<!DOCTYPE html>
<html lang="en">
<head>
<meta charset="utf-8">
<title>Desk Vigor – Active Seating Slides</title>
<link rel="stylesheet" href="https://fonts.googleapis.com/css2?family=Cabin:wght@700&display=swap">
<style>
  :root {
    --page-bg: #ffffff;
    --divider: #111111;
    --orange-light: #fbb62a;
    --orange-mid: #f39a17;
    --orange-deep: #dd6410;
    --glow: #fde0a8;
    --posture-chair-light: #3b3d42;
    --posture-chair-dark: #16171a;
    --core-chair-light: #7a7d82;
    --core-chair-dark: #2c2e32;
    --seating-chair-light: #57524e;
    --seating-chair-dark: #231f1d;
    --headline: #ffffff;
    --headline-shadow: rgba(60, 25, 0, 0.9);
  }
  * { box-sizing: border-box; margin: 0; padding: 0; }
  html, body {
    width: 809px;
    height: 1200px;
    overflow: hidden;
    background: var(--page-bg);
  }
  .slides {
    position: relative;
    width: 809px;
    height: 1200px;
  }
  .slide {
    position: absolute;
    left: 0;
    width: 800px;
    height: 390px;
    border-radius: 0 8px 8px 0;
    overflow: hidden;
    background:
      radial-gradient(ellipse 40% 50% at 22% 52%, var(--glow) 0%, rgba(253,224,168,0) 70%),
      radial-gradient(ellipse 75% 95% at 55% 50%, var(--orange-light) 0%, var(--orange-mid) 45%, var(--orange-deep) 100%);
  }
  .slide--posture  { top: 0; height: 388px; }
  .slide--core     { top: 398px; border-left: 3px solid var(--divider); }
  .slide--seating  { top: 798px; border-left: 3px solid var(--divider); }
  .divider {
    position: absolute;
    left: 0;
    width: 809px;
    height: 4px;
    background: var(--divider);
  }
  .divider--one   { top: 391px; }
  .divider--two   { top: 791px; }
  .divider--three { top: 1191px; }

  .chair-photo { position: absolute; }
  .chair-photo--backrest {
    left: 96px; top: 18px; width: 264px; height: 344px;
    border-radius: 38% 52% 14% 14% / 22% 48% 10% 10%;
    background: radial-gradient(ellipse at 58% 48%, var(--posture-chair-light) 0%, var(--posture-chair-dark) 78%);
  }
  .chair-photo--side {
    left: 96px; top: 20px; width: 264px; height: 354px;
    border-radius: 20% 50% 12% 12% / 16% 44% 8% 8%;
    background: radial-gradient(ellipse at 55% 40%, var(--core-chair-light) 0%, var(--core-chair-dark) 80%);
  }
  .chair-photo--backless {
    left: 106px; top: 32px; width: 262px; height: 326px;
    border-radius: 50% 50% 12% 12% / 44% 44% 8% 8%;
    background: radial-gradient(ellipse at 48% 32%, var(--seating-chair-light) 0%, var(--seating-chair-dark) 80%);
  }

  .headline {
    position: absolute;
    font-family: "Cabin", "Trebuchet MS", sans-serif;
    font-weight: 700;
    font-size: 55px;
    line-height: 72px;
    white-space: nowrap;
    color: var(--headline);
    text-shadow: 2px 2px 2px var(--headline-shadow), 0 0 3px var(--headline-shadow);
  }
  .slide--posture .headline { left: 430px; top: 98px; }
  .slide--core    .headline { left: 406px; top: 4px; }
  .slide--seating .headline { right: 12px; bottom: 26px; text-align: right; }
</style>
</head>
<body>
  <main class="slides">
    <section class="slide slide--posture">
      <div class="chair-photo chair-photo--backrest" role="img" aria-label="Black ball chair with tall adjustable backrest on a five-wheeled base"></div>
      <h2 class="headline">Improve your<br>posture...</h2>
    </section>
    <div class="divider divider--one"></div>

    <section class="slide slide--core">
      <div class="chair-photo chair-photo--side" role="img" aria-label="Grey ball chair with curved side backrest on a wheeled base, side view"></div>
      <h2 class="headline">Improve your<br>core strength...</h2>
    </section>
    <div class="divider divider--two"></div>

    <section class="slide slide--seating">
      <div class="chair-photo chair-photo--backless" role="img" aria-label="Backless dark exercise ball chair resting in a wheeled base"></div>
      <h2 class="headline">The Revolution<br>in Office Seating</h2>
    </section>
    <div class="divider divider--three"></div>
  </main>
</body>
</html>
```